My portfolio needs a makeover! Clean, modern portfolio website needed for tech professional

I need a modern, updated design for my existing portfolio site (https://mirelvoss.folioplace.example/). I am a content professional who has done a lot of different types of content work for big companies. I don't really have a title.

I want to stay simple and clean, but also can be a little whimsical, fun, and a little colorful to go along with the logo I just selected.

I have a domain on Wordpress (mirelvoss.example), but I’d be willing to move my domain to another site for the right design.

I would like it coded/configured and deployed, but I need the ability to update the site myself later to easily switch out my portfolio pieces. I’m not very good at html/xml.

Pages needed:
Home page
Who I am
How to reach me
What I do > By Craft (in the nav, this will be a dropdown under What I Do)
What I do > By Brand (in the nav, this will be a dropdown under What I Do)

Please see Website Design Doc for details!

Requirements
Must have
• Design must include these pages:
1. Homepage
2. Who I Am
3. What I Do
- By Brand
- By Craft
4. How to Reach Me
Nice to have
• Example portfolio sites I like:
https://www.vornaledger.example/
http://lunadrexel.example/
https://www.tjworvan.example/
https://www.orrinbalquist.example/

For my portfolio pieces, I like either tiles or a carousel.

```html
<!DOCTYPE html>
<html lang="en">
<head>
<meta charset="utf-8">
<title>How to Reach Me — Mirel Voss</title>
<link href="https://fonts.googleapis.com/css2?family=Open+Sans:ital,wght@0,400;0,600;1,400&display=swap" rel="stylesheet">
<style>
  :root {
    --navy: #172f3d;
    --footer-navy: #12374d;
    --sky: #2ca6da;
    --sky-soft: #d5ecf7;
    --white: #ffffff;
    --ink: #333333;
    --muted: #8a8a8a;
    --red: #e3001b;
    --field-border: #e2e2e2;
  }
  * { box-sizing: border-box; margin: 0; padding: 0; }
  html, body { width: 1158px; height: 1200px; overflow: hidden; }
  body { position: relative; background: var(--white); font-family: "Open Sans", sans-serif; color: var(--ink); }
  a { text-decoration: none; }

  .site-header { position: absolute; left: 0; top: 0; width: 1158px; height: 80px; background: var(--navy); }
  .brand { position: absolute; left: 100px; top: 31px; display: flex; align-items: center; gap: 7px; color: var(--sky); font-weight: 600; font-size: 13px; letter-spacing: .5px; }
  .brand-dot { width: 12px; height: 12px; border-radius: 50%; background: var(--sky); }
  .main-nav a, .footer-nav a { position: absolute; color: var(--white); font-size: 14.5px; white-space: nowrap; }
  .main-nav a { top: 31px; }
  .main-nav .is-current::after { content: ""; position: absolute; left: -2px; right: -2px; top: 46px; height: 3px; background: var(--sky); }

  .social-mark { position: absolute; display: flex; align-items: center; justify-content: center; border-radius: 50%; background: var(--white); color: var(--navy); font-weight: 600; font-size: 9px; }

  .hero { position: absolute; left: 0; top: 80px; width: 1158px; height: 377px; background: var(--sky); }
  .portrait { position: absolute; left: 510px; top: 34px; width: 144px; height: 144px; border-radius: 50%; border: 5px solid var(--white); background: radial-gradient(circle at 50% 45%, #c9a48c 0%, #8a4a2c 45%, #6f7a6a 100%); }
  .hero-name { position: absolute; left: 0; width: 1158px; top: 186px; text-align: center; color: var(--red); font-weight: 600; font-size: 25px; letter-spacing: .5px; }
  .hero-role { position: absolute; left: 0; width: 1158px; top: 219px; text-align: center; color: var(--white); font-size: 14px; }

  .contact-card { position: absolute; left: 96px; top: 348px; width: 965px; height: 668px; background: var(--white); border-radius: 6px; box-shadow: 0 2px 6px rgba(0,0,0,.12); }
  .card-title { position: absolute; left: 0; width: 965px; top: 52px; text-align: center; font-weight: 400; font-size: 29px; color: var(--ink); }
  .card-intro { position: absolute; left: 152px; width: 696px; top: 132px; text-align: center; font-size: 14px; line-height: 18px; }

  .email-art { position: absolute; left: 152px; top: 256px; width: 103px; height: 95px; border-radius: 4px; background: var(--sky-soft); }
  .email-address { position: absolute; left: 152px; top: 356px; font-size: 14px; }
  .network-link { position: absolute; left: 152px; top: 403px; display: flex; align-items: center; gap: 12px; color: var(--sky); font-weight: 600; font-size: 16px; }
  .network-dot { width: 103px; height: 103px; border-radius: 50%; background: var(--sky); }

  .contact-form .field { position: absolute; left: 525px; width: 322px; background: var(--white); border: 1px solid var(--field-border); border-radius: 5px; box-shadow: 0 2px 4px rgba(0,0,0,.12); padding: 16px 18px; font: italic 12.5px "Open Sans", sans-serif; color: var(--muted); }
  .field-name { top: 273px; height: 47px; }
  .field-email { top: 335px; height: 47px; }
  .field-message { top: 398px; height: 98px; }
  .submit-button { position: absolute; left: 679px; top: 513px; width: 168px; height: 51px; border: 0; border-radius: 26px; background: var(--sky); color: var(--white); font: 600 14px "Open Sans", sans-serif; letter-spacing: .5px; }

  .site-footer { position: absolute; left: 0; top: 1117px; width: 1158px; height: 83px; background: var(--footer-navy); }
  .copyright { position: absolute; left: 100px; top: 33px; color: var(--white); font-size: 13px; }
  .footer-nav a { top: 33px; }
</style>
</head>
<body>
  <header class="site-header">
    <div class="brand"><span class="brand-dot"></span>MIREL VOSS</div>
    <nav class="main-nav">
      <a href="#" style="left:320px">HOME</a>
      <a href="#" style="left:428px">WHO I AM</a>
      <a href="#" style="left:563px">WHAT I DO</a>
      <a href="#" class="is-current" style="left:703px">HOW TO REACH ME</a>
    </nav>
    <a class="social-mark" href="#" style="left:1008px;top:15px;width:50px;height:50px">Linkvault</a>
  </header>

  <section class="hero">
    <div class="portrait" role="img" aria-label="Portrait photo of Mirel Voss"></div>
    <h1 class="hero-name">MIREL VOSS</h1>
    <p class="hero-role">Profesional Content Creator</p>
  </section>

  <main class="contact-card">
    <h2 class="card-title">WORK WITH ME</h2>
    <p class="card-intro">I’d love to hear from you! If you have questions, comments, or just want to geek out over all things content, please reach out.</p>

    <div class="email-art" role="img" aria-label="Open envelope illustration for email contact"></div>
    <p class="email-address">mirel.voss@mailbox.example</p>
    <a class="network-link" href="#"><span class="network-dot"></span>Linkvault</a>

    <form class="contact-form">
      <div class="field field-name">Name *</div>
      <div class="field field-email">Email *</div>
      <div class="field field-message">Message *</div>
      <button class="submit-button" type="button">SUBMIT</button>
    </form>
  </main>

  <footer class="site-footer">
    <p class="copyright">©2020 Mirel Voss. All rights reserved.</p>
    <nav class="footer-nav">
      <a href="#" style="left:429px">HOME</a>
      <a href="#" style="left:536px">WHO I AM</a>
      <a href="#" style="left:671px">WHAT I DO</a>
      <a href="#" style="left:811px">HOW TO REACH ME</a>
    </nav>
    <a class="social-mark" href="#" style="left:1008px;top:16px;width:50px;height:50px">Linkvault</a>
  </footer>
</body>
</html>
```